hobby beef jerky maker looking to break into the commercial market

We need product labels designed for each flavour of jerky we make. Currently have 3 flavours that we are ready to share with the world. We need in your face designs to help us stand out from an already crowded market.
The product name is Rivet Beef Jerky.
The flavours we offer have been named Porch Lope, Ember Glaze and Chili Knack.
The Rivet Beef Jerky Title should remain the same across the three labels but the design for each flavour can change as you see fit.
Label needs to fit within 110mm x 110mm to suit our current packaging

Industry/Entity Type

Food Production

Logo Text

Morvendale Apiary

Colors

Designer to choose colors to be used in the design.

Requirements
Must have
• "Rivet Beef Jerky" font and colour must remain the same across the 3 designs
Nice to have
• The labels will be used on the clear side of the packaging with a small space towards the bottom being left visible so the product inside can be seen

```html
<!DOCTYPE html>
<html lang="en">
<head>
<meta charset="utf-8">
<title>Rivet Beef Jerky – Flavour Labels</title>
<link rel="stylesheet" href="https://fonts.googleapis.com/css2?family=Arvo:wght@400;700&family=Cabin:wght@400&display=swap">
<style>
  :root {
    --ink: #3a1114;
    --paper: #ffffff;
    --hide: #d8c7c9;
    --porch-lope: #5b7a57;
    --ember-glaze: #b9a64f;
    --chili-knack: #bd5352;
    --stamp-text: #ffffff;
  }
  * { box-sizing: border-box; margin: 0; padding: 0; }
  html, body { width: 1200px; height: 1200px; overflow: hidden; background: var(--paper); }
  .canvas { position: relative; width: 1200px; height: 1200px; }

  .label {
    position: absolute;
    width: 461px; height: 461px;
    background: var(--paper);
    border: 6px solid var(--ink);
    overflow: hidden;
  }
  .label--porch-lope  { left: 94px;  top: 106px; --flavour: var(--porch-lope); }
  .label--ember-glaze { left: 648px; top: 106px; --flavour: var(--ember-glaze); }
  .label--chili-knack { left: 372px; top: 614px; --flavour: var(--chili-knack); }

  .label__rule {
    position: absolute; inset: 5px;
    border: 1px dotted var(--ink);
    pointer-events: none;
    z-index: 3;
  }

  .label__backdrop {
    position: absolute;
    left: 12px; top: 64px; right: -4px; bottom: -4px;
    background: linear-gradient(100deg, rgba(216,199,201,0) 0%, var(--hide) 30%, var(--hide) 100%);
    border-top-left-radius: 60% 45%;
    z-index: 1;
  }

  .label__brand {
    position: absolute;
    left: 127px; top: 110px; width: 240px;
    text-align: center;
    font-family: "Arvo", Georgia, serif;
    font-weight: 700;
    font-size: 36px;
    line-height: 1.15;
    color: var(--ink);
    z-index: 2;
  }

  .label__flavour {
    position: absolute;
    left: 96px; top: 311px; width: 276px; height: 76px;
    display: flex; align-items: center; justify-content: center;
    background: var(--flavour);
    outline: 4px dotted var(--flavour);
    outline-offset: 1px;
    font-family: "Arvo", Georgia, serif;
    font-size: 25px;
    letter-spacing: 0.5px;
    text-transform: uppercase;
    color: var(--stamp-text);
    z-index: 2;
  }

  .label__weight {
    position: absolute;
    right: 26px; top: 410px;
    font-family: "Cabin", "Gill Sans", sans-serif;
    font-size: 22px;
    color: var(--ink);
    z-index: 2;
  }
</style>
</head>
<body>
<main class="canvas">

  <section class="label label--porch-lope">
    <div class="label__backdrop" role="img" aria-label="Large faint steer silhouette behind the label"></div>
    <h1 class="label__brand">Rivet<br>Beef<br>Jerky</h1>
    <p class="label__flavour">Porch Lope</p>
    <p class="label__weight">100 g</p>
    <div class="label__rule"></div>
  </section>

  <section class="label label--ember-glaze">
    <div class="label__backdrop" role="img" aria-label="Large faint steer silhouette behind the label"></div>
    <h1 class="label__brand">Rivet<br>Beef<br>Jerky</h1>
    <p class="label__flavour">Ember Glaze</p>
    <p class="label__weight">100 g</p>
    <div class="label__rule"></div>
  </section>

  <section class="label label--chili-knack">
    <div class="label__backdrop" role="img" aria-label="Large faint steer silhouette behind the label"></div>
    <h1 class="label__brand">Rivet<br>Beef<br>Jerky</h1>
    <p class="label__flavour">Chili Knack</p>
    <p class="label__weight">100 g</p>
    <div class="label__rule"></div>
  </section>

</main>
</body>
</html>
```